Buch-/eBook-Cover für populär-wissenschaftliches Buch
Zielgruppe
Der Talgrund-Verlag veröffentlicht Bücher zu psychologischen Themen. Dies ist ein eher populär wissenschaftliches Buch für eine breite Leserschaft.
Aufgabenstellung
Benötigt wird ein Buchcover für KTZ, Papierformat 158*223, Buchformat 154 x 3 x 217 mm 272 Normseiten
Kurzbeschreibung
Am Ufer getragen?
Fragen sich die Autoren Konrad Brüning und Matthias Oswerk. Zwei Psychoanalytiker mit langer Berufserfahrung. Geht das überhaupt: in Liebe und vereint zu sein? Dazu müssen zunächst andere Fragen geklärt werden.
Was vereint die Geschlechter, was bringt sie zusammen? Liebe? Dieses Wort gab es im Deutschen im frühen Mittelalter nicht, erst im späteren. In manchen Kulturen gibt es dieses Wort bis heute nicht, und dennoch leben Mann und Frau zusammen. Schon seit Jahrtausenden beschäftigt sich der Mensch mit der Beziehung zwischen den Geschlechtern. Philosophen, Schriftsteller, Dichter, Maler, Musiker, später Psychoanalytiker, Anthropologen und Soziologen hat die Beziehung zwischen Mann und Frau intensiv beschäftigt. Auch die Religionen befassen sich mit der Beziehung zwischen den Geschlechtern und zeigen vorwiegend auf moralischen und idealistischen Ebenen Umgangsweisen und Lebensformen zwischen den Geschlechtern auf.
280 Normseiten
Bitte Klappentext auf Rückseite

```html
<!DOCTYPE html>
<html lang="de">
<head>
<meta charset="utf-8">
<title>Am Ufer getragen? – Buchcover</title>
<link rel="stylesheet" href="https://fonts.googleapis.com/css2?family=DM+Serif+Display&family=Libre+Caslon+Text&display=swap">
<style>
  :root {
    --cover-red: #d92b1e;
    --paper: #ffffff;
    --ink: #1a1a1a;
    --tone-navy: #1f2a52;
    --tone-blue: #3c5fa0;
    --tone-yellow: #f2b632;
    --tone-orange: #e8772a;
    --tone-red: #d9332a;
  }
  html, body {
    margin: 0;
    padding: 0;
    overflow: hidden;
    background: var(--paper);
  }
  .canvas {
    position: relative;
    width: 975px;
    height: 1200px;
    background: var(--paper);
    overflow: hidden;
  }
  .cover {
    position: absolute;
    left: 140px;
    top: 112px;
    width: 685px;
    height: 970px;
    box-sizing: border-box;
    border: 16px solid var(--cover-red);
    background: var(--paper);
  }
  .cover-title {
    position: absolute;
    left: 0;
    right: 0;
    top: 62px;
    margin: 0;
    text-align: center;
    font-family: "DM Serif Display", Georgia, serif;
    font-weight: 400;
    font-size: 84px;
    line-height: 82px;
    color: var(--cover-red);
    letter-spacing: -0.5px;
  }
  .cover-title .question-mark {
    display: block;
    font-family: "Libre Caslon Text", Georgia, serif;
    font-size: 56px;
    line-height: 70px;
    margin-top: 4px;
  }
  .cover-illustration {
    position: absolute;
    left: 81px;
    top: 290px;
    width: 500px;
    height: 460px;
  }
  .author-list {
    position: absolute;
    left: 46px;
    top: 796px;
    margin: 0;
    padding: 0;
    list-style: none;
    font-family: "Libre Caslon Text", Georgia, serif;
    font-size: 25px;
    line-height: 46px;
    color: var(--ink);
  }
  .publisher-name {
    position: absolute;
    left: 450px;
    width: 180px;
    top: 808px;
    margin: 0;
    text-align: center;
    font-family: "Libre Caslon Text", Georgia, serif;
    font-size: 21px;
    line-height: 30px;
    color: var(--ink);
  }
</style>
</head>
<body>
<div class="canvas">
  <section class="cover">
    <h1 class="cover-title">Am Ufer<br>getragen<span class="question-mark">?</span></h1>

    <svg class="cover-illustration" viewBox="0 0 500 460" role="img"
         aria-label="Herzförmiges, kubistisch gemaltes Bild zweier einander zugewandter Köpfe in Blau, Gelb, Rot und Schwarz">
      <defs>
        <linearGradient id="heart-tones" x1="0" y1="0" x2="1" y2="1">
          <stop offset="0" stop-color="var(--tone-navy)"/>
          <stop offset="0.3" stop-color="var(--tone-blue)"/>
          <stop offset="0.52" stop-color="var(--tone-yellow)"/>
          <stop offset="0.75" stop-color="var(--tone-orange)"/>
          <stop offset="1" stop-color="var(--tone-red)"/>
        </linearGradient>
      </defs>
      <path d="M250 82 C 205 8, 0 0, 0 150 C 0 285, 170 360, 250 455 C 330 360, 500 285, 500 150 C 500 0, 295 8, 250 82 Z"
            fill="url(#heart-tones)"/>
    </svg>

    <ul class="author-list">
      <li>Konrad Brüning</li>
      <li>Matthias Oswerk</li>
    </ul>

    <p class="publisher-name">Talgrund<br>Verlag</p>
  </section>
</div>
</body>
</html>
```